Company that organizes sports leagues needs a poster for one of those leagues

We need to make a poster in A3 format to promote a sports league. I uploaded a file called league in which we have mounted all the information that the poster has to contain. Please do not consider the design of the poster in the league file, it is simply an orientation. It is a guide for the designer to know the text and images that should include. The designers must adapt the design; the text font and the harmony of the poster. The files that CAN NOT be modified are the rest of the files uploaded (logos, images and drawings)
Requirements
Must have
- The text, logos, images and drawings contained in the league file

```html
<!DOCTYPE html>
<html lang="es">
<head>
<meta charset="utf-8">
<title>Liga Padel – Póster</title>
<link rel="stylesheet" href="https://fonts.googleapis.com/css2?family=Anton&family=Roboto+Condensed:wght@400;700&display=swap">
<style>
  :root{
    --page:#eeeeec;
    --green-light:#e3eedd;
    --green-soft:#a9cc9b;
    --green-mid:#6aa65c;
    --green-deep:#2f7a34;
    --green-dark:#1c5522;
    --yellow:#f2e21a;
    --navy:#1d2a4a;
    --white:#ffffff;
    --ink:#1f3b22;
  }
  *{box-sizing:border-box;margin:0;padding:0}
  html,body{width:1200px;height:1200px;overflow:hidden;background:var(--page)}
  body{font-family:"Roboto Condensed",Arial,sans-serif;position:relative}
  .poster{position:absolute;left:300px;top:40px;width:600px;height:1120px;overflow:hidden;
    background:linear-gradient(180deg,var(--green-light) 0%,var(--green-soft) 35%,var(--green-mid) 62%,var(--green-deep) 80%);
    box-shadow:0 6px 18px rgba(0,0,0,.18)}

  .brand{position:absolute;left:16px;top:16px;display:flex;align-items:center;gap:8px;z-index:3;
    background:var(--white);padding:8px 12px;border-radius:4px}
  .brand-mark{width:14px;height:14px;background:var(--navy)}
  .brand-name{font-weight:700;font-size:20px;color:var(--navy);letter-spacing:.5px}

  .splash{position:absolute;left:120px;top:0;width:420px;height:330px;border-radius:0 0 60px 120px;
    background:linear-gradient(160deg,#4f9a47 0%,var(--green-deep) 100%);opacity:.85}
  .figure{position:absolute;border-radius:60px 60px 18px 18px}
  .figure.lead{left:190px;top:20px;width:150px;height:240px;background:linear-gradient(180deg,#c9ced8 0%,var(--navy) 100%)}
  .figure.player{left:395px;top:80px;width:140px;height:220px;background:linear-gradient(180deg,#b9c2b6 0%,#33413a 100%)}
  .figure.officer{left:30px;top:370px;width:120px;height:215px;background:linear-gradient(180deg,#aab3c6 0%,#1b2234 100%)}
  .figure.firefighter{left:440px;top:320px;width:110px;height:200px;background:linear-gradient(180deg,#c4b49a 0%,#2a2620 100%)}

  .title-band{position:absolute;left:20px;top:275px;width:290px;height:72px;background:var(--yellow);z-index:2;
    transform:rotate(-9deg);display:flex;align-items:center;justify-content:center;box-shadow:0 4px 0 var(--green-dark)}
  .title-band span{font-family:"Anton",Impact,sans-serif;font-size:48px;color:var(--green-deep);letter-spacing:1px}

  .category{position:absolute;left:200px;top:385px;color:var(--white);font-weight:700;line-height:1.35;z-index:2}
  .category .gender{font-size:18px}
  .category .audience{font-size:16px}
  .start-label{position:absolute;left:195px;top:460px;background:var(--green-deep);color:var(--white);
    font-weight:700;font-size:21px;padding:3px 14px;z-index:2}
  .start-date{position:absolute;left:180px;top:515px;font-family:"Anton",Impact,sans-serif;font-size:50px;line-height:1;
    color:var(--yellow);letter-spacing:1px;z-index:2}

  .features{position:absolute;left:26px;top:600px;list-style:none;color:var(--white);font-size:14px;line-height:22px}
  .features li::before{content:"›";color:var(--yellow);font-weight:700;margin-right:7px}

  .price{position:absolute;left:368px;top:660px;width:204px;height:70px;background:var(--navy);border-radius:6px;
    color:var(--white);display:flex;align-items:center;justify-content:center;gap:10px;transform:rotate(-3deg)}
  .price .label{font-weight:700;font-size:22px}
  .price .amount{font-family:"Anton",Impact,sans-serif;font-size:32px;color:var(--yellow);line-height:1}
  .price .unit{display:block;font-size:11px;color:var(--white);font-family:"Roboto Condensed",Arial,sans-serif}
  .early{position:absolute;left:375px;top:760px;width:196px;border:2px dashed var(--yellow);padding:8px 10px;
    color:var(--white);font-weight:700;font-size:17px;line-height:1.25;transform:rotate(-3deg)}
  .early .late{color:var(--yellow)}

  .crowd{position:absolute;left:0;top:840px;width:600px;height:110px;
    background:linear-gradient(180deg,rgba(28,85,34,0) 0%,var(--green-dark) 55%,var(--green-dark) 100%)}

  .footer{position:absolute;left:0;top:950px;width:600px;height:170px;background:var(--white)}
  .signup{position:absolute;left:14px;top:16px;background:var(--yellow);color:var(--navy);font-weight:700;
    font-size:15px;padding:5px 12px;border-radius:14px;border:2px solid var(--navy)}
  .contact{position:absolute;left:190px;top:16px;width:390px;display:flex;justify-content:space-between;
    font-size:13px;color:var(--ink);line-height:19px}
  .sponsors{position:absolute;left:0;top:100px;width:600px;height:44px;display:flex;align-items:center;gap:10px;padding:0 8px}
  .tag{background:var(--green-deep);color:var(--white);font-weight:700;font-size:13px;padding:6px 10px;border-radius:12px}
  .badge{height:28px;border-radius:4px;background:#cfd8cf}
  .badge.wide{width:70px}.badge.mid{width:50px}
  .badge.accent{background:#e3e7f0}
  .spacer{flex:1}
</style>
</head>
<body>
  <main class="poster">
    <div class="splash" role="img" aria-label="Mancha verde de pincel detrás de los personajes"></div>
    <div class="figure lead" role="img" aria-label="Personaje con sombrero de copa señalando al frente"></div>
    <div class="figure player" role="img" aria-label="Jugador con dos palas de pádel"></div>
    <div class="figure officer" role="img" aria-label="Agente de policía con pala de pádel"></div>
    <div class="figure firefighter" role="img" aria-label="Bombero con equipo de protección"></div>

    <div class="brand"><span class="brand-mark"></span><span class="brand-name">COURT LEAGUE</span></div>

    <div class="title-band"><span>LIGA PADEL</span></div>

    <div class="category">
      <p class="gender">MASCULINA - FEMENINA</p>
      <p class="audience">Para Fuerzas + Bomberos</p>
    </div>

    <p class="start-label">Inicio de la liga</p>
    <p class="start-date">octubre 2019</p>

    <ul class="features">
      <li>Liga regional</li>
      <li>Juego en su localidad</li>
      <li>Clasificación por puntos y fases</li>
      <li>Premios para los campeones</li>
      <li>Flexibilidad horaria</li>
      <li>Partidos de liga todo el año</li>
      <li>Grupos por nivel de juego</li>
      <li>Welcome pack para todos los participantes</li>
    </ul>

    <div class="price">
      <span class="label">Precio</span>
      <span class="amount">16,85€<span class="unit">por persona</span></span>
    </div>

    <div class="early">
      <p>hasta el 31 de agosto</p>
      <p class="late">después 19€</p>
    </div>

    <div class="crowd" role="img" aria-label="Silueta de público celebrando con un trofeo"></div>

    <footer class="footer">
      <span class="signup">INSCRIPCIONES</span>
      <div class="contact">
        <div><p>liga.courtleague.es</p><p>Court League</p></div>
        <p>600 123 456</p>
      </div>
      <div class="sponsors">
        <span class="tag">Patrocinan</span>
        <span class="badge wide"></span>
        <span class="badge mid accent"></span>
        <span class="badge wide"></span>
        <span class="spacer"></span>
        <span class="badge mid"></span>
        <span class="badge mid accent"></span>
        <span class="tag">Organiza</span>
      </div>
    </footer>
  </main>
</body>
</html>
```